Vape case graphic design

We are looking to create unique design with pattern prints for our Vape case.

The appearance is required to be dynamic and layered, also our theme is related to ice, we need the ice feeling. And we need the design which is matched with European and America style.

We attached our Vape case size and shape for your reference. Pls put your design on the vape case, not just give us the plain design artwork.

Target Market(s)

European and American market

Industry/Entity Type

Vape

```html
<!DOCTYPE html>
<html lang="en">
<head>
<meta charset="utf-8">
<title>Vape Case – Ice Edition</title>
<link href="https://fonts.googleapis.com/css2?family=Montserrat:wght@400;700;800&display=swap" rel="stylesheet">
<style>
  :root {
    --paper: #ffffff;
    --ice-deep: #1d4a6b;
    --ice-mid: #3f7fa6;
    --ice-light: #8cc3de;
    --ice-pale: #b9dcec;
    --cap-silver: #e4e7ea;
    --cap-shade: #b8bdc2;
    --type-white: #ffffff;
    --type-accent: #d2d11a;
  }
  * { margin: 0; padding: 0; box-sizing: border-box; }
  html, body {
    width: 800px;
    height: 1200px;
    overflow: hidden;
    background: var(--paper);
  }
  .canvas {
    position: relative;
    width: 800px;
    height: 1200px;
    font-family: "Montserrat", sans-serif;
  }
  .case-art {
    position: absolute;
    left: 0;
    top: 0;
  }
  .case-title {
    position: absolute;
    left: 291px;
    top: 196px;
    font-weight: 800;
    font-size: 31px;
    line-height: 33px;
    letter-spacing: 0.2px;
  }
  .case-title .title-top { display: block; color: var(--type-white); }
  .case-title .title-bottom { display: block; color: var(--type-accent); }
  .case-tagline {
    position: absolute;
    left: 290px;
    top: 284px;
    writing-mode: vertical-rl;
    text-orientation: upright;
    color: var(--type-white);
    font-weight: 800;
    font-size: 12.5px;
    letter-spacing: 1.6px;
  }
  .case-volume {
    position: absolute;
    left: 455px;
    top: 528px;
    color: var(--type-white);
    font-weight: 400;
    font-size: 12px;
    letter-spacing: 0.3px;
  }
  .texture-band {
    position: absolute;
    left: 0;
    top: 708px;
    width: 800px;
    height: 492px;
    background:
      radial-gradient(ellipse 40% 35% at 75% 30%, rgba(185,220,236,0.55), transparent 70%),
      radial-gradient(ellipse 35% 40% at 20% 70%, rgba(29,74,107,0.6), transparent 70%),
      linear-gradient(135deg, var(--ice-mid) 0%, var(--ice-light) 35%, var(--ice-mid) 60%, var(--ice-deep) 100%);
  }
</style>
</head>
<body>
  <main class="canvas">
    <svg class="case-art" width="800" height="700" viewBox="0 0 800 700" xmlns="http://www.w3.org/2000/svg">
      <defs>
        <linearGradient id="capMetal" x1="0" y1="0" x2="1" y2="0">
          <stop offset="0" stop-color="var(--cap-shade)"/>
          <stop offset="0.5" stop-color="var(--cap-silver)"/>
          <stop offset="1" stop-color="var(--cap-shade)"/>
        </linearGradient>
        <linearGradient id="iceFill" x1="0" y1="0" x2="1" y2="1">
          <stop offset="0" stop-color="#2c6189"/>
          <stop offset="0.35" stop-color="#4f93b8"/>
          <stop offset="0.6" stop-color="#2f6a92"/>
          <stop offset="0.85" stop-color="#5a9fc2"/>
          <stop offset="1" stop-color="#1f4d70"/>
        </linearGradient>
      </defs>
      <rect class="case-cap" x="297" y="80" width="98" height="24" rx="3" fill="url(#capMetal)"/>
      <path class="case-body" role="img" aria-label="Close-up texture of blue ice crystals covering the case"
        fill="url(#iceFill)"
        d="M300,100 H390 Q398,100 398,108 V148 Q398,165 414,165 H502 Q520,165 520,183 V554 Q520,572 502,572 H284 Q266,572 266,554 V183 Q266,165 276,165 Q292,165 292,148 V108 Q292,100 300,100 Z"/>
    </svg>

    <h1 class="case-title">
      <span class="title-top">LOREM</span>
      <span class="title-bottom">IPSUM</span>
    </h1>
    <p class="case-tagline">DOLOR SIT AMET</p>
    <p class="case-volume">10ML</p>

    <div class="texture-band" role="img" aria-label="Seamless pattern of blue ice crystal texture"></div>
  </main>
</body>
</html>
```